依頼詳細
興味を持ってもらい中の資料を読んで頂くのが目的ですので「マジシャンのプロダクション業者である」「女性マジシャンに力を入れている」ということが分かり、「ここは面白そうだから、中に入っている詳しい資料を見たい」と思って頂けるようなデザインをお願いします。
記載項目
PLYエンターテインメント
http://ply-t.jp/
大阪府和泉市緑ヶ丘6-4-17
0725-41-2866
サイズ
A4
ページ数
片面
希望イメージ
• +5 0 +5
• シンプル
複雑
• 単色
カラフル
• 暗い
明るい
• 日常
高級
• 遊び心
厳粛
• 未来的
伝統的
• 女性的
男性的
希望する色
納品ファイル
• 高解像度JPG (.jpg)
• PNG形式 (.png)
補足説明
こちらで提供する写真を素材としてお使いください。ファイルが数枚ありますので、zip ファイルに固めました。以下よりダウンロードください。
https://www.filevault-share.jp/s/k3v9q0w2xr7mzpb/%E7%94%BB%E5%83%8F%E7%B4%A0%E6%9D%90.zip?dl=0
依頼公開後の追記内容
■ 選んだ理由

こちらのイメージにあった高級感とインパクトがあったことが理由となります。

■ 提案者全員のお礼・コメント

さまざまなご提案をありがとうございました。思ったよりも多くの方に応募いただき助かりました。今後ともよろしくお願いいたします。

```html
<!DOCTYPE html>
<html lang="ja">
<head>
<meta charset="utf-8">
<title>PLYエンターテインメント</title>
<link href="https://fonts.googleapis.com/css2?family=Anton&family=Noto+Sans+JP:wght@400;700;900&display=swap" rel="stylesheet">
<style>
:root{
  --bg-deep:#1a0618;
  --bg-mid:#5a1248;
  --title-hi:#fff0fa;
  --title-mid:#ff8fd0;
  --title-lo:#c2177c;
  --title-edge:#6b0a44;
  --card:#fbf8f4;
  --card-line:#d9c9b3;
  --red:#d1203a;
  --ink:#1d1d1d;
  --bar:#17131a;
  --bar-text:#ffffff;
}
*{margin:0;padding:0;box-sizing:border-box}
html,body{width:849px;height:1200px;overflow:hidden;background:var(--bg-deep)}
.poster{
  position:relative;width:849px;height:1200px;overflow:hidden;
  background:
    radial-gradient(ellipse 60% 35% at 50% 30%, rgba(255,110,190,.55), transparent 70%),
    radial-gradient(circle at 15% 20%, rgba(255,120,200,.35), transparent 25%),
    radial-gradient(circle at 85% 45%, rgba(255,200,120,.25), transparent 25%),
    radial-gradient(circle at 10% 70%, rgba(255,90,170,.3), transparent 22%),
    radial-gradient(circle at 92% 80%, rgba(255,120,200,.25), transparent 22%),
    linear-gradient(180deg, #3a0b33 0%, var(--bg-mid) 40%, #2a0824 75%, var(--bg-deep) 100%);
  font-family:"Noto Sans JP",sans-serif;
}
.stage-floor{
  position:absolute;left:-60px;right:-60px;top:640px;height:480px;
  background:
    repeating-linear-gradient(90deg, rgba(255,255,255,.06) 0 2px, transparent 2px 70px),
    repeating-linear-gradient(0deg, rgba(255,255,255,.05) 0 2px, transparent 2px 60px),
    linear-gradient(180deg, rgba(120,20,90,.4), rgba(20,5,20,.9));
  transform:perspective(500px) rotateX(45deg);
  transform-origin:top;
}
.bokeh{position:absolute;border-radius:50%;background:radial-gradient(circle, rgba(255,200,235,.7), rgba(255,120,200,0) 70%)}
.loose-card{position:absolute;width:60px;height:86px;background:rgba(255,255,255,.85);border:2px solid var(--card-line);border-radius:5px}
.title{
  position:absolute;left:30px;top:48px;width:789px;text-align:center;
  font-family:"Anton",sans-serif;line-height:.92;
}
.title-line{
  display:block;letter-spacing:3px;white-space:nowrap;
  background:linear-gradient(180deg,var(--title-hi) 0%,var(--title-mid) 45%,var(--title-lo) 100%);
  -webkit-background-clip:text;background-clip:text;color:transparent;
  filter:drop-shadow(0 6px 0 var(--title-edge)) drop-shadow(0 0 14px rgba(255,100,190,.7));
}
.title-line.l1{font-size:150px}
.title-line.l2{font-size:145px}
.title-line.l3{font-size:140px}
.title-line.l4{font-size:96px;letter-spacing:2px;margin-top:4px}
.card{
  position:absolute;background:var(--card);border:3px solid var(--card-line);
  border-radius:10px;box-shadow:0 10px 24px rgba(0,0,0,.55);padding:24px 18px;
}
.card .photo{width:100%;height:100%;border:2px solid var(--red);border-radius:3px}
.card .rank{position:absolute;font-family:"Anton",sans-serif;font-size:20px;line-height:1;color:var(--red);text-align:center}
.card .rank.black{color:var(--ink)}
.card .rank.tl{left:5px;top:4px}
.card .rank.br{right:5px;bottom:4px;transform:rotate(180deg)}
.info-bar{
  position:absolute;left:0;bottom:0;width:849px;height:96px;background:var(--bar);
  color:var(--bar-text);display:flex;align-items:center;padding:0 26px;gap:22px;
}
.brand{display:flex;align-items:center;gap:8px;font-weight:900;font-size:34px;letter-spacing:1px}
.brand-dot{width:14px;height:14px;border-radius:50%;background:var(--bar-text)}
.company{flex:1}
.company-name{font-weight:700;font-size:22px}
.company-address{font-size:13px;margin-top:4px}
.contact{text-align:right}
.contact-tel{display:flex;align-items:center;justify-content:flex-end;gap:6px;font-weight:700;font-size:27px}
.contact-row{display:flex;align-items:center;justify-content:flex-end;gap:10px;margin-top:4px;font-size:11px}
.search-box{display:flex;align-items:center;border:1px solid #fff;font-size:10px}
.search-box span{padding:2px 6px}
.search-box .btn{background:#fff;color:var(--bar)}
</style>
</head>
<body>
<div class="poster">
  <div class="stage-floor"></div>

  <div class="bokeh" style="left:20px;top:120px;width:90px;height:90px"></div>
  <div class="bokeh" style="left:720px;top:60px;width:110px;height:110px"></div>
  <div class="bokeh" style="left:40px;top:560px;width:70px;height:70px"></div>
  <div class="bokeh" style="left:760px;top:520px;width:80px;height:80px"></div>

  <div class="loose-card" style="left:30px;top:320px;transform:rotate(-30deg)"></div>
  <div class="loose-card" style="left:780px;top:250px;transform:rotate(25deg)"></div>
  <div class="loose-card" style="left:60px;top:1010px;transform:rotate(20deg)"></div>
  <div class="loose-card" style="left:745px;top:740px;transform:rotate(-18deg)"></div>

  <h1 class="title">
    <span class="title-line l1">PRISM</span>
    <span class="title-line l2">LADIES</span>
    <span class="title-line l3">YARD</span>
    <span class="title-line l4">ENTERTAINMENT</span>
  </h1>

  <div class="card" style="left:160px;top:640px;width:150px;height:205px;transform:rotate(-14deg)">
    <div class="photo" role="img" aria-label="女性マジシャンのポートレート写真" style="background:linear-gradient(160deg,#e9d8c8,#b58a6e)"></div>
    <span class="rank tl">A<br>♥</span><span class="rank br">A<br>♥</span>
  </div>
  <div class="card" style="left:345px;top:625px;width:150px;height:200px;transform:rotate(-4deg)">
    <div class="photo" role="img" aria-label="女性マジシャンのポートレート写真" style="background:linear-gradient(160deg,#d3b7a8,#6a3a44)"></div>
    <span class="rank tl black">K<br>♠</span><span class="rank br black">K<br>♠</span>
  </div>
  <div class="card" style="left:625px;top:615px;width:160px;height:230px;transform:rotate(10deg)">
    <div class="photo" role="img" aria-label="ピエロ姿のマジシャンの写真" style="background:linear-gradient(160deg,#f2c6d8,#d2506e)"></div>
    <span class="rank tl">Q<br>♦</span><span class="rank br">Q<br>♦</span>
  </div>
  <div class="card" style="left:160px;top:840px;width:180px;height:220px;transform:rotate(-5deg)">
    <div class="photo" role="img" aria-label="女性マジシャンのポートレート写真" style="background:linear-gradient(160deg,#f0e2d6,#a57d66)"></div>
    <span class="rank tl black">J<br>♣</span><span class="rank br black">J<br>♣</span>
  </div>
  <div class="card" style="left:345px;top:825px;width:170px;height:250px;transform:rotate(4deg)">
    <div class="photo" role="img" aria-label="女性マジシャンのポートレート写真" style="background:linear-gradient(160deg,#e6d0c2,#4a2a2e)"></div>
    <span class="rank tl">Q<br>♥</span><span class="rank br">Q<br>♥</span>
  </div>
  <div class="card" style="left:585px;top:890px;width:130px;height:205px;transform:rotate(-5deg)">
    <div class="photo" role="img" aria-label="女性マジシャンのポートレート写真" style="background:linear-gradient(160deg,#f3d8c0,#c0624a)"></div>
    <span class="rank tl black">A<br>♠</span><span class="rank br black">A<br>♠</span>
  </div>

  <footer class="info-bar">
    <div class="brand"><span class="brand-dot"></span>PLY</div>
    <div class="company">
      <div class="company-name">PLYエンターテインメント</div>
      <div class="company-address">〒594-0041 大阪府和泉市緑ヶ丘6-4-17</div>
    </div>
    <div class="contact">
      <div class="contact-tel">
        <svg width="22" height="22" viewBox="0 0 24 24" aria-hidden="true"><path fill="#fff" d="M6.6 10.8a15 15 0 0 0 6.6 6.6l2.2-2.2a1 1 0 0 1 1-.25 11.4 11.4 0 0 0 3.6.57 1 1 0 0 1 1 1V20a1 1 0 0 1-1 1A17 17 0 0 1 3 4a1 1 0 0 1 1-1h3.5a1 1 0 0 1 1 1c0 1.25.2 2.45.57 3.57a1 1 0 0 1-.25 1z"/></svg>
        TEL : 0725-41-2866
      </div>
      <div class="contact-row">
        <span>http://ply-t.jp/</span>
        <span class="search-box"><span>PLYエンターテインメント</span><span class="btn">検索</span></span>
      </div>
    </div>
  </footer>
</div>
</body>
</html>
```